Brookmere Recovery Center Billboard (Addiction / Alcohol / Opioid )

visit www.brookmererecovery-example.com
We are an inpatient treatment center for opioid, alcohol and drug addiction. We are looking to get multiple 12'x25' billboards in our area. Our Phone number is 1-855-CALM-NOW we are located in Auburn Indiana
We pride ourselves on a comfortable medical detox and treat our patients as family.

Target Market(s)

Current Addicts, Addicts family or friends, Factory Workers and Shopvane shoppers

Industry/Entity Type

Health Care

Font styles to use
Sans Serif

Colors
0355a3
3176b5
ffffff

Requirements
Must have
• Logo and Phone number, and Brookmere Recovery
Nice to have
• Ideas?
1.) Addiction hurts more than yourself. (Pic of little girl?)
2.) Just how much are you willing to lose?
3.) Addiction does not define you, You are what you choose to become.
4.) Indiana's most comfortable Detox
5.) Detox in unmatched comfort.
6.) Background could be patient room with logo in upper right
7.) Looking to be able to read easily from road.
Should not have
• Hard to read lettering

```html
<!DOCTYPE html>
<html lang="en">
<head>
<meta charset="utf-8">
<title>Brookmere Recovery Billboard</title>
<link rel="stylesheet" href="https://fonts.googleapis.com/css2?family=Anton&family=Montserrat:wght@700;800&display=swap">
<style>
  :root {
    --navy: #283061;
    --cyan: #35b6e4;
    --white: #ffffff;
    --ink: #3a3a3a;
    --backdrop: #e4e4e4;
  }
  html, body {
    margin: 0;
    width: 1200px;
    height: 1200px;
    overflow: hidden;
    background: var(--backdrop);
  }
  .billboard { display: block; }
  .headline-top { font-family: "Anton", "Oswald", sans-serif; fill: var(--white); }
  .headline-main { font-family: "Anton", "Oswald", sans-serif; fill: var(--cyan); }
  .location { font-family: "Montserrat", Arial, sans-serif; font-weight: 800; fill: var(--navy); }
  .phone { font-family: "Montserrat", Arial, sans-serif; font-weight: 700; fill: var(--ink); }
  .brand-name { font-family: "Montserrat", Arial, sans-serif; font-weight: 700; fill: var(--navy); }
</style>
</head>
<body>
<svg class="billboard" width="1200" height="1200" viewBox="0 0 1200 1200" xmlns="http://www.w3.org/2000/svg">
  <defs>
    <linearGradient id="hero-tone" x1="0" y1="0" x2="1" y2="0">
      <stop offset="0" stop-color="#35b6e4"/>
      <stop offset="0.28" stop-color="#6fa9c8"/>
      <stop offset="0.45" stop-color="#c9c9c9"/>
      <stop offset="0.6" stop-color="#8d8d8d"/>
      <stop offset="0.78" stop-color="#4a4f72"/>
      <stop offset="1" stop-color="#283061"/>
    </linearGradient>
    <linearGradient id="room-tone" x1="0" y1="0" x2="0" y2="1">
      <stop offset="0" stop-color="#eceef0"/>
      <stop offset="0.55" stop-color="#c4c7cb"/>
      <stop offset="0.7" stop-color="#b89c7c"/>
      <stop offset="1" stop-color="#9c7e5f"/>
    </linearGradient>
    <radialGradient id="ground-shadow" cx="0.5" cy="0.5" r="0.5">
      <stop offset="0" stop-color="#000" stop-opacity="0.22"/>
      <stop offset="1" stop-color="#000" stop-opacity="0"/>
    </radialGradient>
    <filter id="soft-shadow" x="-15%" y="-15%" width="130%" height="135%">
      <feDropShadow dx="0" dy="4" stdDeviation="4" flood-opacity="0.25"/>
    </filter>
  </defs>

  <g class="board" transform="translate(30 338)">
    <rect class="board-bg" width="1140" height="523" fill="var(--white)"/>
    <rect class="headline-band" x="0" y="145" width="1140" height="227" fill="var(--navy)"/>

    <!-- hero circle -->
    <ellipse cx="268" cy="490" rx="220" ry="16" fill="url(#ground-shadow)"/>
    <circle cx="268" cy="274" r="253" fill="var(--white)"/>
    <circle cx="268" cy="274" r="243" fill="url(#hero-tone)" role="img"
            aria-label="Black and white photo of a little girl sitting on steps holding a leaf, over a blue circle"/>

    <!-- facility room photos -->
    <g class="room-photo" filter="url(#soft-shadow)">
      <circle cx="117" cy="417" r="78" fill="var(--white)"/>
      <circle cx="117" cy="417" r="71" fill="url(#room-tone)" role="img" aria-label="Patient bedroom with two beds"/>
    </g>
    <g class="room-photo" filter="url(#soft-shadow)">
      <circle cx="416" cy="411" r="77" fill="var(--white)"/>
      <circle cx="416" cy="411" r="70" fill="url(#room-tone)" role="img" aria-label="Patient bedroom with dresser and wall TV"/>
    </g>
    <g class="room-photo" filter="url(#soft-shadow)">
      <circle cx="273" cy="446" r="78" fill="var(--white)"/>
      <circle cx="273" cy="446" r="71" fill="url(#room-tone)" role="img" aria-label="Lounge with massage chairs"/>
    </g>

    <!-- brand -->
    <g class="brand">
      <circle cx="649" cy="80" r="50" fill="var(--cyan)"/>
      <text class="brand-name" x="730" y="80" font-size="34" textLength="253" lengthAdjust="spacingAndGlyphs">BROOKMERE</text>
      <text class="brand-name" x="731" y="104" font-size="13" textLength="252" lengthAdjust="spacing">RECOVERY</text>
    </g>

    <!-- headline -->
    <text class="headline-top" x="552" y="207" font-size="54" textLength="479" lengthAdjust="spacingAndGlyphs">ADDICTION HURTS MORE THAN</text>
    <text class="headline-main" x="552" y="349" font-size="164" textLength="479" lengthAdjust="spacingAndGlyphs">YOURSELF</text>

    <!-- location and phone -->
    <text class="location" x="552" y="433" font-size="38" textLength="479" lengthAdjust="spacing">AUBURN INDIANA</text>
    <g class="phone-icon">
      <circle cx="574" cy="466" r="22" fill="var(--cyan)"/>
      <path d="M566 455 q-4 3 -1 10 q4 9 12 13 q6 3 9 -1 l-5 -5 q-2 2 -4 1 q-5 -3 -7 -8 q-1 -2 1 -4 z" fill="var(--white)"/>
    </g>
    <text class="phone" x="616" y="482" font-size="47" textLength="415" lengthAdjust="spacingAndGlyphs">1-855-CALM-NOW</text>
  </g>
</svg>
</body>
</html>
```